Request for Business Card Design

Hi. My name is Marlena, I am looking for a new business card design for my company, Quillbrook Sensing Systems, LLC. I really like the design you did for Tavel Harvest and was hoping you could do something similar using our full logo and our mark. I am also open to any raised texture design using our mark. I have attached our full logo, which would need to be somewhere on the card, as well as the mark in both outline and full form, as well as our brand colors / guide. The card does not have to be white, as long as our logo and mark appear. I actually like darker colored business cards more, but am open to all options. If you are interested in working with me, please let me know. We would also take the business card design into letterhead design if you can do that.

```html
<!DOCTYPE html>
<html lang="en">
<head>
<meta charset="utf-8">
<title>Quillbrook Sensing Systems — Business Card</title>
<link rel="stylesheet" href="https://fonts.googleapis.com/css2?family=Roboto:wght@400;500;700&display=swap">
<style>
  :root {
    --brand-blue: #1b9cc4;
    --brand-blue-light: #25afd2;
    --brand-blue-deep: #1484ad;
    --ink: #262a2e;
    --ink-soft: #3d4247;
    --paper: #ffffff;
    --backdrop: #5d6670;
  }
  * { margin: 0; padding: 0; box-sizing: border-box; }
  html, body { width: 1200px; height: 900px; overflow: hidden; }
  body {
    background: var(--backdrop);
    font-family: "Roboto", Arial, sans-serif;
    display: flex;
    align-items: center;
    justify-content: center;
    gap: 60px;
  }
  .card {
    width: 510px;
    height: 292px;
    border-radius: 24px;
    position: relative;
    overflow: hidden;
    box-shadow: 0 10px 30px rgba(0,0,0,0.3);
  }

  /* Back side */
  .card-back { background: var(--brand-blue); }
  .back-texture {
    position: absolute; inset: 0;
    background: linear-gradient(135deg, var(--brand-blue-deep) 0%, var(--brand-blue-light) 55%, var(--brand-blue) 100%);
  }
  .back-wordmark {
    position: absolute; left: 50%; top: 50%;
    transform: translate(-50%, -50%);
    display: flex; align-items: center; gap: 14px;
    color: var(--paper);
  }
  .wordmark-dot {
    width: 40px; height: 40px; border-radius: 50%;
    flex: none;
  }
  .back-wordmark .wordmark-dot { background: var(--paper); }
  .wordmark-text {
    font-weight: 700;
    line-height: 1.05;
    text-transform: uppercase;
  }
  .wordmark-name { display: block; font-size: 30px; letter-spacing: 2px; }
  .wordmark-tag { display: block; font-size: 10px; letter-spacing: 0.6px; margin-top: 3px; }

  /* Front side */
  .card-front { background: var(--paper); color: var(--ink); }
  .holder {
    position: absolute; left: 0; top: 34px;
    padding-left: 24px;
    border-left: 6px solid var(--brand-blue);
  }
  .holder-name { font-size: 20px; font-weight: 700; letter-spacing: 0.5px; text-transform: uppercase; }
  .holder-role { font-size: 15px; color: var(--ink-soft); margin-top: 2px; }
  .divider {
    position: absolute; left: 22px; right: 70px; top: 116px;
    height: 1.5px; background: var(--brand-blue);
  }
  .contacts { position: absolute; left: 24px; top: 134px; list-style: none; }
  .contacts li {
    display: flex; align-items: center; gap: 10px;
    font-size: 14px; color: var(--ink-soft); margin-bottom: 7px;
  }
  .contact-icon {
    width: 16px; height: 16px; border-radius: 50%;
    background: var(--brand-blue);
    display: flex; align-items: center; justify-content: center;
    flex: none;
  }
  .front-wordmark {
    position: absolute; right: 28px; top: 40px;
    display: flex; align-items: center; gap: 12px;
    color: var(--ink);
  }
  .front-wordmark .wordmark-dot { background: var(--brand-blue); width: 36px; height: 36px; }
  .front-wordmark .wordmark-name { font-size: 26px; }
  .front-wordmark .wordmark-tag { font-size: 9px; }
  .address {
    position: absolute; right: 70px; bottom: 40px;
    font-size: 15px; color: var(--ink-soft); line-height: 1.5; text-align: left;
  }
</style>
</head>
<body>

  <section class="card card-back" aria-label="Card back">
    <div class="back-texture" role="img" aria-label="Blue gradient with faint raised pattern of the brand mark"></div>
    <div class="back-wordmark">
      <span class="wordmark-dot"></span>
      <span class="wordmark-text">
        <span class="wordmark-name">Quillbrook</span>
        <span class="wordmark-tag">Sensing Systems</span>
      </span>
    </div>
  </section>

  <section class="card card-front" aria-label="Card front">
    <div class="holder">
      <p class="holder-name">Owen Hartley</p>
      <p class="holder-role">Director</p>
    </div>

    <div class="front-wordmark">
      <span class="wordmark-dot"></span>
      <span class="wordmark-text">
        <span class="wordmark-name">Quillbrook</span>
        <span class="wordmark-tag">Sensing Systems</span>
      </span>
    </div>

    <div class="divider"></div>

    <ul class="contacts">
      <li>
        <span class="contact-icon">
          <svg width="10" height="10" viewBox="0 0 24 24" aria-hidden="true"><path fill="#fff" d="M6.6 10.8a15.1 15.1 0 0 0 6.6 6.6l2.2-2.2c.3-.3.7-.4 1-.2 1.1.4 2.3.6 3.6.6.6 0 1 .4 1 1V20c0 .6-.4 1-1 1A17 17 0 0 1 3 4c0-.6.4-1 1-1h3.5c.6 0 1 .4 1 1 0 1.3.2 2.5.6 3.6.1.3 0 .7-.2 1z"/></svg>
        </span>
        +65 9123 4567
      </li>
      <li>
        <span class="contact-icon">
          <svg width="10" height="10" viewBox="0 0 24 24" aria-hidden="true"><path fill="#fff" d="M3 5h18v14H3zm2 2v.4l7 4.6 7-4.6V7zm0 2.8V17h14V9.8l-7 4.6z"/></svg>
        </span>
        owen@quillbrook.com.sg
      </li>
      <li>
        <span class="contact-icon">
          <svg width="10" height="10" viewBox="0 0 24 24" aria-hidden="true"><circle cx="12" cy="12" r="9" fill="none" stroke="#fff" stroke-width="2"/><path d="M3 12h18M12 3c3 3 3 15 0 18M12 3c-3 3-3 15 0 18" fill="none" stroke="#fff" stroke-width="1.6"/></svg>
        </span>
        www.quillbrook.com.sg
      </li>
    </ul>

    <address class="address" style="font-style: normal;">
      1480 Alder Crest Dr.suite 310<br>
      Maple Ridge,TX 75001
    </address>
  </section>

</body>
</html>
```